Junior tennis development pathway graphic

The National Racquet Sport Union(NRSU) and the Global Court Games Council (GCGC)
recommend (read demand) that all junior tennis programs now be ran using a progressive format of 4 different colored balls, different court sizes and scoring systems for various ages. We want to create a graphic for our juniors page on our web site that will show parents in a VERY EASY to understand way how their kids will progress through the various stages of tennis. The page is being built using Bootstrap and we plan to use jQuerry Hotspot to give detailed information over certain areas of the graphic. This specific information will be Dbase driven with class names,and specific class info. - The design does not need to show this, I just though it might be helpful to know
Updates

There are 2 other sites that will be helpful in understanding this project:

The first is www.smallplayerscourt.com and the second is my junior page on my current website
www.pinebrookracquetclub.com/juniora.cfm

I added a new file named jr pathway 2

This is an idea i had for the project - needs to be completed and given some sizzle

Target Market(s)

Parents of children ages 3-16

Industry/Entity Type

Progressive

Requirements
Must have
• Vector format
800x800 pixels max
EASY TO UNDERSTAND
Use of some or all of the key words and phrases in the uploaded file "keywords"
Should not have
• I do not want it to look like every other development graphic already out there.
To see what is currently being used image search
"tennis pathway" or "junior tennis pathway"

"pathway and" juniorspathway" in the uploaded files section are 2 ideas of VERY bad attempts

```html
<!DOCTYPE html>
<html lang="en">
<head>
<meta charset="utf-8">
<title>Junior Tennis Development Pathway</title>
<link rel="stylesheet" href="https://fonts.googleapis.com/css2?family=Bree+Serif&display=swap">
<style>
  :root{
    --navy:#131a45;
    --red-text:#e0201b;
    --band-learn:#272d36;
    --band-play:#07a553;
    --band-compete:#1565a7;
    --tile-green:#7bbb3f;
    --tile-orange:#ff6a00;
    --tile-red:#e2323a;
    --tile-yellow:#dfa915;
    --ball:#d4e12b;
    --white:#ffffff;
  }
  *{margin:0;padding:0;box-sizing:border-box}
  html,body{width:1200px;height:1200px;overflow:hidden;background:#fff}
  .pathway{position:relative;width:1200px;height:1200px;overflow:hidden;font-family:"Bree Serif",Georgia,serif}
  .header{position:absolute;left:0;top:0;width:1200px;height:163px;background:linear-gradient(#ffffff,#e9e9ea)}
  .racquet-art{position:absolute;left:12px;top:6px;width:200px;height:130px;border-radius:50% 50% 40% 40%;background:radial-gradient(ellipse at 60% 40%,#f2f2f2,#c4c4c4)}
  .tagline-small{position:absolute;left:70px;top:136px;font-size:17px;color:#333;white-space:nowrap}
  .title{position:absolute;left:248px;top:24px;font-weight:400;font-size:55px;color:var(--navy);white-space:nowrap;-webkit-text-stroke:1.2px var(--navy)}
  .subtitle{position:absolute;left:0;width:1424px;top:96px;text-align:center;font-weight:400;font-size:33px;color:var(--red-text);white-space:nowrap}
  .band{position:absolute;left:0;width:1200px}
  .band-learn{top:163px;height:263px;background:var(--band-learn)}
  .band-play{top:426px;height:262px;background:var(--band-play)}
  .band-compete{top:688px;height:512px;background:var(--band-compete)}
  .step{position:absolute;color:var(--white);font-weight:400;line-height:1;white-space:nowrap;-webkit-text-stroke:2px var(--white)}
  .step .num,.step .verb{display:block}
  .step-learn{left:62px;top:228px}
  .step-learn .num{font-size:68px}
  .step-learn .verb{font-size:70px;margin-top:10px}
  .step-play{left:60px;top:486px}
  .step-play .num{font-size:66px}
  .step-play .verb{font-size:86px;margin-top:2px}
  .step-compete{left:913px;top:776px}
  .step-compete .num{font-size:70px}
  .step-compete .verb{font-size:52px;margin-top:12px}
  .links{position:absolute;left:0;top:0}
  .ball{position:absolute;width:108px;height:108px;border-radius:50%}
  .ball-green{background:radial-gradient(circle at 42% 58%,var(--ball) 62%,var(--tile-green) 100%)}
  .ball-orange{background:radial-gradient(circle at 42% 58%,var(--ball) 62%,var(--tile-orange) 100%)}
  .ball-red{background:radial-gradient(circle at 42% 58%,var(--ball) 62%,var(--tile-red) 100%)}
  .ball-yellow{background:radial-gradient(circle at 42% 58%,#f2c21e 62%,var(--tile-yellow) 100%)}
  .tile{position:absolute;width:202px;height:97px;color:var(--white);text-align:center;font-size:16px;line-height:20.5px;padding-top:8px;
        clip-path:polygon(0 0,100% 0,97% 50%,100% 100%,0 100%,3% 50%)}
  .tile .name{display:block;font-size:15px}
  .tile-green{background:var(--tile-green)}
  .tile-orange{background:var(--tile-orange)}
  .tile-red{background:var(--tile-red)}
  .tile-yellow{background:var(--tile-yellow)}
  .program-title{position:absolute;left:0;width:1484px;top:1008px;text-align:center;font-weight:400;font-size:46px;color:#eef2f7;white-space:nowrap;-webkit-text-stroke:1px #eef2f7}
  .program-item{position:absolute;width:300px;text-align:center;color:var(--white);font-size:22px;white-space:nowrap}
</style>
</head>
<body>
<main class="pathway">
  <header class="header">
    <div class="racquet-art" role="img" aria-label="Illustration of a tennis racquet"></div>
    <p class="tagline-small">4 COLORS - 1 GAME</p>
    <h1 class="title">Junior Tennis Development Pathway</h1>
    <p class="subtitle">“your child’s path to success at every level (age)”</p>
  </header>

  <section class="band band-learn"></section>
  <section class="band band-play"></section>
  <section class="band band-compete"></section>

  <h2 class="step step-learn"><span class="num">STEP 1</span><span class="verb">LEARN</span></h2>
  <h2 class="step step-play"><span class="num">STEP 2</span><span class="verb">PLAY</span></h2>
  <h2 class="step step-compete"><span class="num">STEP 3</span><span class="verb">COMPETE</span></h2>

  <div class="ball ball-green" style="left:396px;top:191px" role="img" aria-label="Green tennis ball illustration"></div>
  <div class="ball ball-orange" style="left:696px;top:191px" role="img" aria-label="Orange tennis ball illustration"></div>
  <div class="ball ball-red" style="left:996px;top:191px" role="img" aria-label="Red tennis ball illustration"></div>
  <div class="ball ball-green" style="left:396px;top:451px" role="img" aria-label="Green tennis ball illustration"></div>
  <div class="ball ball-orange" style="left:696px;top:451px" role="img" aria-label="Orange tennis ball illustration"></div>
  <div class="ball ball-red" style="left:996px;top:451px" role="img" aria-label="Red tennis ball illustration"></div>
  <div class="ball ball-yellow" style="left:96px;top:711px" role="img" aria-label="Yellow tennis ball illustration"></div>
  <div class="ball ball-green" style="left:396px;top:711px" role="img" aria-label="Green tennis ball illustration"></div>
  <div class="ball ball-orange" style="left:696px;top:711px" role="img" aria-label="Orange tennis ball illustration"></div>
  <div class="ball ball-yellow" style="left:96px;top:971px" role="img" aria-label="Yellow tennis ball illustration"></div>

  <svg class="links" width="1200" height="1200" viewBox="0 0 1200 1200" aria-hidden="true">
    <defs>
      <marker id="head" viewBox="0 0 10 10" refX="6" refY="5" markerWidth="4.4" markerHeight="4.4" orient="auto">
        <path d="M0 0 L10 5 L0 10 L3 5 Z" fill="#fff"/>
      </marker>
    </defs>
    <g stroke="#fff" stroke-width="4" fill="none" marker-end="url(#head)">
      <line x1="652" y1="350" x2="596" y2="350"/>
      <line x1="955" y1="350" x2="892" y2="350"/>
      <line x1="538" y1="398" x2="538" y2="472"/>
      <line x1="836" y1="398" x2="836" y2="472"/>
      <line x1="1136" y1="398" x2="1136" y2="472"/>
      <line x1="655" y1="608" x2="596" y2="608"/>
      <line x1="948" y1="608" x2="892" y2="608"/>
      <line x1="352" y1="660" x2="294" y2="726"/>
      <line x1="538" y1="658" x2="538" y2="734"/>
      <line x1="650" y1="660" x2="589" y2="736"/>
      <line x1="836" y1="660" x2="836" y2="734"/>
      <line x1="655" y1="870" x2="592" y2="870"/>
      <line x1="355" y1="870" x2="294" y2="870"/>
      <line x1="238" y1="920" x2="238" y2="988"/>
    </g>
  </svg>

  <div class="tile tile-green" style="left:349px;top:300px"><span class="name">GREEN 1</span>Age : 5-8 Years<br>Court Size : 36X18<br>Racquet Size : 36X18</div>
  <div class="tile tile-orange" style="left:649px;top:300px"><span class="name">ORANDE 1</span>Age : 5-8 Years<br>Court Size : 36X18<br>Racquet Size : 36X18</div>
  <div class="tile tile-red" style="left:949px;top:300px"><span class="name">RED 1</span>Age : 5-8 Years<br>Court Size : 36X18<br>Racquet Size : 36X18</div>

  <div class="tile tile-green" style="left:349px;top:560px"><span class="name">JUNIOR TENNIS LEAGUE</span>Age : 5-8 Years<br>Court Size : 36X18<br>Racquet Size : 36X18</div>
  <div class="tile tile-orange" style="left:649px;top:560px"><span class="name">ORANGE 2</span>Age : 5-8 Years<br>Court Size : 36X18<br>Racquet Size : 36X18</div>
  <div class="tile tile-red" style="left:949px;top:560px"><span class="name">RED 2</span>Age : 5-8 Years<br>Court Size : 36X18<br>Racquet Size : 36X18</div>

  <div class="tile tile-yellow" style="left:49px;top:820px"><span class="name">JTT YELLOW</span>Age : 5-8 Years<br>Court Size : 36X18<br>Racquet Size : 36X18</div>
  <div class="tile tile-green" style="left:349px;top:820px"><span class="name">JTT GREEN</span>Age : 5-8 Years<br>Court Size : 36X18<br>Racquet Size : 36X18</div>
  <div class="tile tile-orange" style="left:649px;top:820px"><span class="name">JTT ORANGE</span>Age : 5-8 Years<br>Court Size : 36X18<br>Racquet Size : 36X18</div>

  <div class="tile tile-yellow" style="left:49px;top:1080px"><span class="name">HIGH SCHOOL TEAM</span>Age : 5-8 Years<br>Court Size : 36X18<br>Racquet Size : 36X18</div>

  <h3 class="program-title">What is a program?</h3>
  <p class="program-item" style="left:330px;top:1094px">-Teaching/Coaching</p>
  <p class="program-item" style="left:627px;top:1094px">-Training/Practicing</p>
  <p class="program-item" style="left:888px;top:1094px">-Competition</p>
  <p class="program-item" style="left:330px;top:1147px">-Play</p>
  <p class="program-item" style="left:627px;top:1147px">-Social</p>
  <p class="program-item" style="left:888px;top:1147px">-Fun</p>
</main>
</body>
</html>
```